Book Cover for Memoir: Sexual Assault and Traumatic Stress

I need a cover design for a memoir that is a victim's story of a sexual assault. I will need a print-on-demand cover, an eBook cover, and a 3D thumbnail image. The thumbnail and eBook cover will be used immediately, and the POD cover will be used in a few months with the full manuscript is ready. Therefore, I need an artist who is willing to make small adjustments if needed once the page count is set.

I have a image I have purchased that should give you an idea of the desired direction, but you can feel free to use your own images. I have attached some examples of book covers I like. I attached a color palette for fonts.

Overall Look: Fonts should be feminine and thin, but large to stand out. Look should be simple and elegant, and display and overall depressing feeling. There should be enough detail though to make it look professionally put together. Not TOO minimalistic.

I have also attached the Paper Loom templates if you choose to use those. If not, ensure there is an open place for the barcode on the bottom right.

Requirements
Must have
• Title: Beneath Quiet Rooms
Subtitle: A Daughter's Record of Silence, Doubt & Mending
Author: Nora Jean Whitfield
Audience: Mostly women 18-30
Quote (for the back): "I always thought I'd know how I'd react if I ever was raped. I was wrong. I've been wrong a lot lately."
Summary (back cover): When twenty-seven-year-old Nora Whitfield wakes up with a gut-wrenching feeling, she has little memory of the horrifying events that occurred the night before. Days earlier, Nora was a spirited single mom who had abandoned her hometown to raise her daughter in the city and pursue her dreams. In the short months since Nora’s move to Seattle, she became the adored lover of a charismatic lawyer, started a new business, and finally felt life was going her way. So what happened to cause her to break?

In a gripping and heartbreaking narrative, Nora tells the true story of how her life unraveled from the traumatic events that took place that night and why what seems obvious to everyone else is impossible for Nora to believe. Beneath Quiet Rooms is a chilling exploration of memory through trauma, trust in humanity, and a captivating story of strength and survival that appeals to the heart of fathers and mothers, sons and daughters, and men and women alike.
Nice to have
• BACK COVER: I'd like to have a photo on the back. This should depict the happy life of the main character before the sexual assault, and should be with her daughter. Or should be a nature scene that starts at the corner and blends into the rest of the cover. I have attached a possible image or you can use something you like.

```html
<!DOCTYPE html>
<html lang="en">
<head>
<meta charset="utf-8">
<title>Beneath Quiet Rooms — Book Cover</title>
<link href="https://fonts.googleapis.com/css2?family=Montserrat:wght@500;600;700;800&display=swap" rel="stylesheet">
<style>
  :root {
    --backdrop: #e9e9ea;
    --paper: #f4f4f5;
    --paper-front: #f7f7f7;
    --ink: #161616;
    --ink-soft: #2b2b2b;
    --placeholder: #e6d9cf;
    --placeholder-ink: #3a3230;
    --spine-edge: #3a3a3a;
    --photo-light: #f1efeb;
    --photo-warm: #e8dccb;
  }
  * { box-sizing: border-box; margin: 0; padding: 0; }
  html, body { width: 1200px; height: 800px; overflow: hidden; }
  body {
    background: var(--backdrop);
    font-family: "Montserrat", Arial, sans-serif;
    color: var(--ink);
  }
  .cover-spread {
    position: absolute;
    left: 125px; top: 50px;
    width: 950px; height: 700px;
    display: flex;
    box-shadow: 0 12px 30px rgba(0,0,0,0.12);
  }
  /* Back cover */
  .back-cover {
    width: 450px; height: 100%;
    background: var(--paper);
    padding: 28px 32px 30px;
    display: flex; flex-direction: column;
  }
  .back-author {
    text-align: right;
    font-weight: 700; font-size: 13px; letter-spacing: 0.4px;
    text-transform: uppercase;
    padding-right: 28px;
  }
  .back-title {
    font-weight: 800; font-size: 25px; letter-spacing: 0.2px;
    text-transform: uppercase; line-height: 1.1; margin-top: 6px;
    white-space: nowrap;
  }
  .back-subtitle {
    font-weight: 700; font-size: 9.6px; text-transform: uppercase;
    letter-spacing: 0.2px; margin-top: 5px;
    white-space: nowrap;
  }
  .back-summary {
    margin-top: 20px;
    font-weight: 700; font-size: 12px; line-height: 1.45;
    text-align: justify; text-align-last: center;
    color: var(--ink-soft);
  }
  .back-summary p + p { margin-top: 2px; }
  .back-quote {
    margin-top: 18px;
    padding: 0 18px;
    font-weight: 600; font-size: 11.5px; line-height: 1.45;
    text-align: center;
    color: var(--ink-soft);
  }
  .back-placeholders {
    margin-top: auto;
    display: flex; justify-content: space-between;
    padding: 0 12px;
  }
  .placeholder-box {
    width: 118px; height: 64px;
    background: var(--placeholder);
    display: flex; align-items: center; justify-content: center;
    font-weight: 700; font-size: 12px; color: var(--placeholder-ink);
  }
  /* Spine */
  .spine {
    position: relative;
    width: 44px; height: 100%;
    background: var(--paper);
    border-left: 1px solid #d4d4d4;
    border-right: 4px solid var(--spine-edge);
  }
  .spine-text {
    position: absolute;
    writing-mode: vertical-rl;
    text-transform: uppercase;
    white-space: nowrap;
  }
  .spine-title { left: 3px; top: 26px; font-weight: 800; font-size: 21px; line-height: 1; }
  .spine-subtitle { left: 26px; top: 26px; font-weight: 600; font-size: 8.4px; line-height: 1; }
  .spine-author { left: 12px; bottom: 28px; font-weight: 700; font-size: 11px; letter-spacing: 0.5px; }
  /* Front cover */
  .front-cover {
    width: 456px; height: 100%;
    background: var(--paper-front);
    display: flex; flex-direction: column;
    padding: 38px 0 28px;
  }
  .front-title {
    padding: 0 20px;
    font-weight: 800; font-size: 29px; letter-spacing: 0.2px;
    text-transform: uppercase; line-height: 1.05;
    white-space: nowrap;
  }
  .front-subtitle {
    padding: 0 20px;
    font-weight: 700; font-size: 11px; text-transform: uppercase;
    letter-spacing: 0.2px; margin-top: 6px;
    white-space: nowrap;
  }
  .cover-photo {
    margin: 28px 0 0 18px;
    width: 420px; height: 470px;
    background: linear-gradient(90deg, var(--photo-light) 0%, var(--photo-warm) 35%, var(--photo-warm) 55%, var(--photo-light) 100%);
  }
  .front-author {
    margin-top: auto;
    text-align: center;
    font-weight: 700; font-size: 13px; letter-spacing: 0.5px;
    text-transform: uppercase;
  }
</style>
</head>
<body>
  <main class="cover-spread">
    <section class="back-cover">
      <div class="back-author">Nora Jean Whitfield</div>
      <h2 class="back-title">Beneath Quiet Rooms</h2>
      <div class="back-subtitle">A Daughter's Record of Silence, Doubt &amp; Mending</div>
      <div class="back-summary">
        <p>When twenty-seven-year-old Nora Whitfield wakes up with a gut-wrenching feeling, she has little memory of the horrifying events that occurred the night before. Days earlier, Nora was a spirited single mom who had abandoned her hometown to raise her daughter in the city and pursue her dreams. In the short months since Nora's move to Seattle, she became the adored lover of a charismatic lawyer, started a new business, and finally felt life was going her way. So what happened to cause her to break?</p>
        <p>In a gripping and heartbreaking narrative, Nora tells the true story of how her life unraveled from the traumatic events that took place that night and why what seems obvious to everyone else is impossible for Nora to believe. Beneath Quiet Rooms is a chilling exploration of memory through trauma, trust in humanity, and a captivating story of strength and survival that appeals to the heart of fathers and mothers, sons and daughters, and men and women alike.</p>
      </div>
      <blockquote class="back-quote">"I always thought I'd know how I'd react if I ever was raped. I was wrong. I've been wrong a lot lately."</blockquote>
      <div class="back-placeholders">
        <div class="placeholder-box">LOGO</div>
        <div class="placeholder-box">ISBN</div>
      </div>
    </section>

    <section class="spine">
      <span class="spine-text spine-title">Beneath Quiet Rooms</span>
      <span class="spine-text spine-subtitle">A Daughter's Record of Silence, Doubt &amp; Mending</span>
      <span class="spine-text spine-author">Nora Jean Whitfield</span>
    </section>

    <section class="front-cover">
      <h1 class="front-title">Beneath Quiet Rooms</h1>
      <div class="front-subtitle">A Daughter's Record of Silence, Doubt &amp; Mending</div>
      <div class="cover-photo" role="img" aria-label="Cover photograph: a woman sitting on a white bed hugging her knees, head bowed, against a pale wall"></div>
      <div class="front-author">Nora Jean Whitfield</div>
    </section>
  </main>
</body>
</html>
```